2 guided dives on the North of Bonaire

2 guided shore dives on the North of Bonaire including authentic local lunch and drinks.
We offer an adventure for experienced divers to discover the dive sites on the north of the island.
Showing you the beauty of the reefs and tasting authentic local cuisine like goat or iguana combined with a stunning view of the surroundings.

Target Market(s)

Divers / tourism

Industry/Entity Type

Tourism / Diving

Font styles to use
Sans Serif

Colors
0054AA
0677BA
7BADD7
CADEEF
E8F1F8
0094D4
00A9DD
6FCCEA
C7EBF8
E9F6FB
F0912C
F2A743
F7CA91
FBE8D2
FDF5EE
EE7325
F08F49
F5BC92
FAE3D3
FDF4ED

Requirements
Must have
• Some of the pictures I uploaded and the food picture / bottom like in the pictures
Nice to have
• inviting to join us on the guided dives
Should not have
• Any picture I didn't provide

```html
<!DOCTYPE html>
<html lang="en">
<head>
<meta charset="utf-8">
<title>Reefline Dive – Guided Dives Flyer</title>
<link href="https://fonts.googleapis.com/css2?family=Montserrat:wght@400;600;800;900&display=swap" rel="stylesheet">
<style>
  :root{
    --navy:#0e2a4a;
    --deep:#0054AA;
    --ocean:#0677BA;
    --sky:#00A9DD;
    --sky-light:#6FCCEA;
    --foam:#C7EBF8;
    --orange:#F0912C;
    --orange-deep:#EE7325;
    --sand:#F7CA91;
    --white:#ffffff;
    --backdrop:#d9d9d9;
  }
  *{box-sizing:border-box;margin:0;padding:0}
  html,body{width:1200px;height:900px;overflow:hidden}
  body{background:var(--backdrop);font-family:'Montserrat',sans-serif;position:relative}
  .flyer{position:absolute;left:295px;top:20px;width:610px;height:860px;background:var(--sky);overflow:hidden;box-shadow:0 10px 30px rgba(0,0,0,.25)}
  .hero{position:absolute;left:0;top:0;width:100%;height:360px;
    background:linear-gradient(180deg,#1d4f78 0%,#1f86a8 28%,#5cc3cf 45%,#cfe8f0 60%,#9ad6f0 75%,var(--sky) 100%)}
  .hero-shore{position:absolute;right:0;top:0;width:210px;height:230px;
    background:linear-gradient(200deg,#5f8a4a 0%,#8aa86a 40%,#e6e0cf 75%,rgba(230,224,207,0) 100%)}
  .badge{position:absolute;right:40px;top:30px;width:80px;height:80px;border-radius:50%;background:var(--deep);opacity:.9}
  .brand{position:absolute;left:34px;top:168px;display:flex;align-items:center;gap:10px}
  .brand-dot{width:44px;height:44px;border-radius:50%;background:var(--orange)}
  .brand-name{font-weight:900;font-size:22px;color:var(--deep)}
  .copy{position:absolute;left:34px;top:226px;width:330px;display:flex;flex-direction:column;gap:12px}
  .title{font-weight:900;font-size:24px;line-height:1.1;color:var(--navy);text-transform:uppercase}
  .content{color:var(--navy);font-size:12px;line-height:1.4}
  .content p{margin-bottom:8px}
  .pill{display:inline-block;background:var(--orange);color:var(--white);font-weight:800;font-size:12px;padding:3px 16px;border-radius:12px;margin-bottom:5px}
  .photos{position:absolute;right:22px;top:250px;width:200px}
  .photo{width:190px;height:150px;border-radius:50%;border:4px solid var(--orange);margin-bottom:-10px}
  .photo.coast{background:linear-gradient(180deg,#5b8fd0 0%,#a9cdee 40%,#2a7fa8 55%,#6f6a62 80%,#5a5650 100%)}
  .photo.food{background:radial-gradient(circle at 40% 45%,#e6a24a 0%,#b9612a 45%,#6b3a22 80%)}
  .photo.beach{background:linear-gradient(180deg,#3f76c8 0%,#bcd7f2 45%,#35a5c4 60%,#e9e3d2 75%,#d9d1bd 100%)}
  .contact{position:absolute;left:330px;top:735px;display:flex;align-items:center;gap:14px;color:var(--navy);font-weight:800;font-size:13px}
  .clock{width:70px;height:70px}
  .line{display:flex;align-items:center;gap:8px}
  .icon{width:20px;height:20px;border-radius:50%;background:var(--orange);display:flex;align-items:center;justify-content:center}
  .social{position:absolute;left:330px;top:815px;display:flex;align-items:center;gap:8px;color:var(--navy);font-weight:800;font-size:13px}
  .social-dot{width:26px;height:26px;border-radius:50%;background:var(--deep)}
  .more{position:absolute;left:34px;top:790px}
  .more .pill{font-size:15px;padding:5px 28px;border-radius:16px}
  .web{display:block;color:var(--navy);font-size:13px;margin-top:6px}
</style>
</head>
<body>
  <main class="flyer">
    <div class="hero" role="img" aria-label="Photo of turquoise sea meeting a rocky white shoreline with green shrubs"></div>
    <div class="hero-shore" role="img" aria-label="Shoreline vegetation"></div>
    <div class="badge" aria-label="Certification badge"></div>

    <div class="brand"><span class="brand-dot"></span><span class="brand-name">Reefline Dive</span></div>

    <div class="copy">
      <h1 class="title">Uncover the underwater wonders of Bonaire</h1>
      <section class="content">
        <p>Embark on a captivating underwater adventure with our expert guides and discover the vibrant marine life and stunning coral reefs of Bonaire's Northside.</p>
        <span class="pill">2 Guided Dives</span>
        <p>Immerse yourself in the depths of the ocean, guided by experienced divers who will unveil the hidden gems of Bonaire's underwater world.</p>
        <span class="pill">Authentic Local Flavor</span>
        <p>After each dive, savor the flavors of Bonaire's cuisine at Casa Vista Alta, where an authentic local lunch awaits.</p>
        <span class="pill">Let Us Take Care of the Rest</span>
        <p>Leave the logistics to us, so you can focus on immersing yourself in the underwater splendor. We'll handle all the equipment, planning, and transportation, ensuring a seamless dive experience.</p>
        <span class="pill">Join Us on This Unforgettable Journey</span>
        <p>Ready to experience the underwater wonders of Bonaire? Contact us today to book your guided dives and embark on this unforgettable journey.</p>
      </section>
    </div>

    <div class="photos">
      <div class="photo coast" role="img" aria-label="Photo of a rocky coast under a blue sky"></div>
      <div class="photo food" role="img" aria-label="Photo of plates of authentic local lunch"></div>
      <div class="photo beach" role="img" aria-label="Photo of a white beach with clear water under a palm roof"></div>
    </div>

    <div class="contact">
      <svg class="clock" viewBox="0 0 70 70" aria-label="Open 24 hours">
        <path d="M35 8 A27 27 0 1 0 62 35" fill="none" stroke="var(--white)" stroke-width="5" stroke-dasharray="4 3"/>
        <circle cx="35" cy="38" r="22" fill="var(--orange)"/>
        <text x="35" y="46" text-anchor="middle" font-family="Montserrat,sans-serif" font-weight="800" font-size="20" fill="var(--white)">24</text>
        <path d="M58 30 L62 36 L66 30" fill="var(--white)"/>
      </svg>
      <div class="line">
        <span class="icon"><svg width="12" height="12" viewBox="0 0 24 24"><path fill="#fff" d="M6.6 10.8a15 15 0 006.6 6.6l2.2-2.2c.3-.3.7-.4 1-.2 1.1.4 2.3.6 3.6.6.6 0 1 .4 1 1V20c0 .6-.4 1-1 1A17 17 0 013 4c0-.6.4-1 1-1h3.5c.6 0 1 .4 1 1 0 1.3.2 2.5.6 3.6.1.3 0 .7-.2 1z"/></svg></span>
        +599-555-0142
      </div>
    </div>

    <div class="social">
      <span class="social-dot"></span>
      <span class="icon"><svg width="12" height="12" viewBox="0 0 24 24"><path fill="#fff" d="M3 5h18v14H3z M3 5l9 7 9-7" stroke="#F0912C" stroke-width="1.5"/></svg></span>
      hello@reefline-dive.com
    </div>

    <div class="more">
      <span class="pill">More Info:</span>
      <span class="web">www.reefline-dive.com</span>
    </div>
  </main>
</body>
</html>
```